Rejuvenate Canada Natural SkinCare Brand packaging box

Tessa Brandt Natural Producat based in Canada B.C.Miss Tessa Brandt is the founder of the company, she is a reflexologist therapist. The hero product are Tessa Brandt Velvet Salve and Massage oil, the product help her clients to allievate many skin problems and sore msucle condition.

The formula of Tessa Brandt Natural Product is based on a recipe that was used by many generations of a Belgium family.The recipe survived the "Chemicalization" of natural remedies as it is believed that pure, natural remedies have superior healing abilities. The recipes used three main herbs: St. John's wort, Calendula and arnica.

We would like to see designs that use our classical green color (brand color) and the three flowers components (St. John's wort, Calendula and arnica) to rejuvenate the packaging. Since we will keep adding new product to the line. We want to see a contemporary, simple and natural design, so that the customer able to recognize our brand and outstanding the product on the shelf.

The Tessa Brandt logo remains or could simply. The 3 flowers could present or use simple graphic or outline.

For details of existing design, please refer www.tessabrandt-example.com.hk

Target Market(s)

For 40-70 women market

Industry/Entity Type

It Company

Font styles to use
Serif

Requirements
Must have
• Tessa Brandt Logo
• Brand green color (RBG R:56 G:152 B:3)
• 3 main flowers ingredients ( in simple graphic/ outline)
• outstanding on the shelf
• Natural, simple and contemporary
• Strong branding
• Not too colorful
• Easily identify different product in the same brand
• (Velvet Salve, Massage oil, face oil, healing balm stick, pain ointment)
Nice to have
• Hot-stamping silver or embossed pattern is optional
• ecologo, no animal test, 100% all natural, vegan, non GMO, paraben free
Should not have
• Too fancy approach

```html
<!DOCTYPE html>
<html lang="en">
<head>
<meta charset="utf-8">
<title>Tessa Brandt Face Cream – Carton Dieline</title>
<link rel="stylesheet" href="https://fonts.googleapis.com/css2?family=Arimo:wght@400;700&family=Noto+Sans+TC:wght@400&display=swap">
<style>
  :root {
    --paper: #ffffff;
    --brand-green: #119a4a;
    --deep-green: #0d8c41;
    --mint: #e6f3e9;
    --maroon: #7a2a22;
    --logo-brown: #6b2f22;
    --copy-shadow: #3a5a44;
    --cut-line: #e0584a;
    --fold-line: #e0584a;
    --petal-orange: #f39a1c;
    --petal-yellow: #f7d21e;
  }
  * { box-sizing: border-box; margin: 0; padding: 0; }
  html, body { width: 1153px; height: 1200px; overflow: hidden; background: var(--paper); }
  body { position: relative; font-family: "Arimo", Arial, sans-serif; }

  .panel {
    position: absolute;
    top: 276px;
    height: 693px;
    background: linear-gradient(to bottom,
      var(--paper) 0%, var(--paper) 20%, var(--mint) 36%,
      #86c79a 52%, #2ea25a 68%, var(--brand-green) 80%, var(--deep-green) 100%);
    overflow: hidden;
  }
  .panel--side   { left: 53px;  width: 194px; }
  .panel--back   { left: 247px; width: 196px; }
  .panel--front  { left: 443px; width: 187px; }
  .panel--cn     { left: 630px; width: 188px; }
  .panel--preview{ left: 898px; width: 196px; border: 1px solid #9fcfae; }

  .front-face > * { position: absolute; left: 0; right: 0; text-align: center; }
  .brand-name {
    top: 76px; font-size: 22px; font-weight: 400; color: var(--logo-brown);
    display: flex; justify-content: center; align-items: center; gap: 6px;
  }
  .brand-dot { width: 9px; height: 9px; border-radius: 50%; background: var(--petal-yellow); }
  .tagline { top: 142px; font-size: 8.5px; color: var(--maroon); }
  .front-face .product-rule { height: 2px; background: var(--brand-green); left: 22px; right: 22px; }
  .front-face .product-rule--top { top: 204px; }
  .front-face .product-rule--bottom { top: 238px; }
  .product-name { top: 212px; font-size: 21px; font-weight: 700; color: var(--brand-green); }
  .variant { top: 266px; font-size: 14px; font-weight: 700; color: var(--maroon); }
  .formula { top: 284px; font-size: 9.5px; font-weight: 700; color: var(--maroon); }
  .front-face .flower-art {
    top: 302px; left: 14px; right: 14px; height: 176px;
    border-radius: 14px;
    background: linear-gradient(135deg, var(--petal-yellow) 0%, #f7b81e 45%, var(--petal-orange) 75%, #f5c418 100%);
  }
  .claim { top: 494px; font-size: 10px; color: #fff; line-height: 1.5; }
  .origin { top: 598px; font-size: 9.5px; font-weight: 700; color: #fff; }
  .volume { top: 644px; font-size: 9px; font-weight: 700; color: #f2d0c8; }

  .copy-block {
    position: absolute; left: 22px; right: 16px; color: #fff;
    font-size: 8.3px; line-height: 1.22;
    text-shadow: 0 0 1px var(--copy-shadow), 0 0 2px var(--copy-shadow), 0 0 2px var(--copy-shadow);
  }
  .copy-block p { margin-bottom: 8px; text-align: justify; }
  .copy-block h4 { font-size: 8.3px; font-weight: 700; }
  .copy-block--back { top: 287px; font-weight: 700; }
  .copy-block--cn { top: 292px; font-family: "Noto Sans TC", sans-serif; font-size: 8.6px; line-height: 1.9; }
  .copy-block--cn p { text-align: left; }
  .distributor { position: absolute; left: 0; right: 0; top: 564px; text-align: center; font-size: 8.5px; color: var(--maroon); line-height: 1.3; }
  .panel--cn .distributor { font-family: "Noto Sans TC", sans-serif; }
  .web-address { position: absolute; left: 0; right: 0; top: 598px; text-align: center; font-size: 9px; font-weight: 700; color: #fff; }

  .dieline { position: absolute; left: 0; top: 0; pointer-events: none; }
  .dieline .cut { fill: none; stroke: var(--cut-line); stroke-width: 1; }
  .dieline .fold { fill: none; stroke: var(--fold-line); stroke-width: .8; stroke-dasharray: 4 3; }
</style>
</head>
<body>

<section class="panel panel--side front-face">
  <div class="brand-name"><span class="brand-dot"></span>Tessa Brandt</div>
  <div class="tagline">FEEL YOUNGER - LOOK YOUNGER</div>
  <div class="product-rule product-rule--top"></div>
  <div class="product-name">FACE CREAM</div>
  <div class="product-rule product-rule--bottom"></div>
  <div class="variant">REJUVENATING</div>
  <div class="formula">Anti -Wrinkle Formula</div>
  <div class="flower-art" role="img" aria-label="Calendula, arnica and St. John's wort flower illustration"></div>
  <div class="claim">100%<br>NATURAL HERBAL<br>INGREDIENTS</div>
  <div class="origin">MADE IN CANADA</div>
  <div class="volume">60mL</div>
</section>

<section class="panel panel--back">
  <div class="copy-block copy-block--back">
    <p>This luxurious anti-wrinkle face cream indulges the skin with uniquely soothing herbal ingredients that moisturize mature dry skin and smoothen wrinkles to visibly reduce the appearance of aging.</p>
    <p>The ingredients in this formula are 100% natural and suitable for any skin type.</p>
    <h4>INGREDIENTS</h4>
    <p>Aloe Barbadensis Leaf Juice, Cetearyl Olivate, Sorbitan Olivate, Calendula Officinalis, Arnica Montana, Hypericum Perforatum Flowers Infused in Vitis Vinifera Seed Oil, Cera Alba, Sodium Stearoyl Lactylate, Rosmarinus Officinalis Leaf, Glucose, Olea Europea, Ginkgo Biloba, Hippophae Rhamnoides Leaf, Calendula Officinalis Flower, Curcuma Longa Rhizome, Lavandula Angustifolia Oil.</p>
    <p>*Certified natural preservative that are derived from natural ingredients.</p>
  </div>
  <div class="distributor">Distributed by: Harbourline Holdings Ltd.<br>T: (852) 2400 1188</div>
  <div class="web-address">www.tessabrandt-example.com.hk</div>
</section>

<section class="panel panel--front front-face">
  <div class="brand-name"><span class="brand-dot"></span>Tessa Brandt</div>
  <div class="tagline">FEEL YOUNGER - LOOK YOUNGER</div>
  <div class="product-rule product-rule--top"></div>
  <div class="product-name">FACE CREAM</div>
  <div class="product-rule product-rule--bottom"></div>
  <div class="variant">REJUVENATING</div>
  <div class="formula">Anti -Wrinkle Formula</div>
  <div class="flower-art" role="img" aria-label="Calendula, arnica and St. John's wort flower illustration"></div>
  <div class="claim">100%<br>NATURAL HERBAL<br>INGREDIENTS</div>
  <div class="origin">MADE IN CANADA</div>
  <div class="volume">60mL</div>
</section>

<section class="panel panel--cn">
  <div class="copy-block copy-block--cn">
    <p>這款奢華抗皺面霜以獨特舒緩的天然草本成分滋潤肌膚，有效滋養成熟乾燥肌膚，撫平細紋，令肌膚重現青春光彩。</p>
    <p>100%天然成份，適合任何皮膚類型。</p>
    <p>成份：<br>蘆薈、橄欖油乳化劑、金盞花、山金車、貫葉連翹、葡萄籽油、蜂蠟、迷迭香葉、葡萄糖、橄欖、銀杏、沙棘葉、金盞花、薑黃、薰衣草精油。</p>
  </div>
  <div class="distributor">總代理：Harbourline Holdings Ltd.<br>電話：(852) 2400 1188</div>
  <div class="web-address">www.tessabrandt-example.com.hk</div>
</section>

<section class="panel panel--preview front-face">
  <div class="brand-name"><span class="brand-dot"></span>Tessa Brandt</div>
  <div class="tagline">FEEL YOUNGER - LOOK YOUNGER</div>
  <div class="product-rule product-rule--top"></div>
  <div class="product-name">FACE CREAM</div>
  <div class="product-rule product-rule--bottom"></div>
  <div class="variant">REJUVENATING</div>
  <div class="formula">Anti -Wrinkle Formula</div>
  <div class="flower-art" role="img" aria-label="Calendula, arnica and St. John's wort flower illustration"></div>
  <div class="claim">100%<br>NATURAL HERBAL<br>INGREDIENTS</div>
  <div class="origin">MADE IN CANADA</div>
  <div class="volume">60mL</div>
</section>

<svg class="dieline" width="1153" height="1200" viewBox="0 0 1153 1200" aria-hidden="true">
  <path class="cut" d="M247,276 L53,276 L53,969 L247,969"/>
  <path class="cut" d="M247,276 L258,222 L433,218 L443,236"/>
  <path class="cut" d="M443,236 L443,90 Q443,33 500,33 L573,33 Q630,33 630,90 L630,236"/>
  <path class="cut" d="M630,236 L640,218 L810,222 L818,276 L818,969"/>
  <path class="cut" d="M247,969 L258,1024 L433,1024 L443,1010"/>
  <path class="cut" d="M443,1010 L443,1160 L630,1160 L630,1010"/>
  <path class="cut" d="M630,1010 L640,1024 L810,1024 L818,969"/>
  <path class="fold" d="M53,276 H818 M53,969 H818"/>
  <path class="fold" d="M247,276 V969 M443,236 V1010 M630,236 V1010"/>
  <path class="fold" d="M443,80 H630 M443,1027 H630"/>
</svg>

</body>
</html>
```